NEW YORK Plumbing/utility company 10 year anniversary business card

Looking For simple back and front business card would like to include a few things in description
We offer 24/7 emergency service
residential
commercial
industrial
municipal
services offered
Plumbing
hydro excavation
hydro jetting
Well pumps
Sewer pumps
water mains
sewer mains

```html
<!DOCTYPE html>
<html lang="en">
<head>
<meta charset="utf-8">
<title>Kestrel Water &amp; Sewer – Business Card</title>
<link href="https://fonts.googleapis.com/css2?family=Arimo:wght@400;700&display=swap" rel="stylesheet">
<style>
  :root {
    --card-blue: #1f64a6;
    --accent-blue: #2ea6e6;
    --ink-white: #ffffff;
    --backdrop: #3a3a3c;
  }
  * { box-sizing: border-box; margin: 0; padding: 0; }
  html, body { width: 1200px; height: 900px; overflow: hidden; }
  body {
    background: var(--backdrop);
    font-family: "Arimo", Arial, sans-serif;
    display: flex; flex-direction: column; align-items: center; justify-content: center; gap: 40px;
  }
  .card {
    position: relative;
    width: 700px; height: 400px;
    background: var(--card-blue);
    border-bottom: 10px solid var(--accent-blue);
    color: var(--ink-white);
    overflow: hidden;
  }
  .brand {
    display: flex; align-items: center; gap: 12px;
    font-weight: 700; color: var(--ink-white);
    letter-spacing: 1px; text-transform: uppercase;
  }
  .brand-dot { width: 18px; height: 18px; border-radius: 50%; background: var(--ink-white); flex: none; }

  /* Front */
  .card-front .brand { position: absolute; top: 90px; left: 0; right: 0; justify-content: center; font-size: 40px; }
  .services { position: absolute; top: 215px; left: 60px; right: 60px; text-align: center; }
  .services-heading {
    display: flex; align-items: center; gap: 18px;
    color: var(--accent-blue); font-weight: 700; font-size: 24px; letter-spacing: 1px; text-transform: uppercase;
  }
  .services-heading::before, .services-heading::after { content: ""; flex: 1; height: 2px; background: var(--accent-blue); }
  .bullet-list { list-style: none; display: flex; flex-wrap: wrap; justify-content: center; gap: 6px 18px; margin-top: 20px; font-size: 20px; }
  .bullet-list li::before { content: "•"; color: var(--accent-blue); margin-right: 6px; }

  /* Back */
  .card-back .brand { position: absolute; top: 150px; left: 40px; width: 310px; font-size: 28px; line-height: 1.15; }
  .divider { position: absolute; left: 370px; top: 70px; width: 2px; height: 200px; background: var(--accent-blue); }
  .contact { position: absolute; left: 400px; top: 70px; }
  .person-name { color: var(--accent-blue); font-weight: 700; font-size: 28px; text-transform: uppercase; }
  .person-role { font-size: 18px; margin-top: 4px; }
  .contact-list { list-style: none; margin-top: 26px; font-size: 18px; display: grid; gap: 10px; }
  .contact-list li { display: flex; align-items: center; gap: 10px; }
  .contact-list svg { width: 16px; height: 16px; fill: var(--accent-blue); flex: none; }
  .offer { position: absolute; left: 0; right: 0; bottom: 28px; text-align: center; }
  .offer-line { color: var(--accent-blue); font-weight: 700; font-size: 26px; }
  .card-back .bullet-list { margin-top: 8px; }
</style>
</head>
<body>
  <section class="card card-front">
    <div class="brand"><span class="brand-dot"></span>Kestrel Water &amp; Sewer</div>
    <div class="services">
      <h2 class="services-heading">Services Offered</h2>
      <ul class="bullet-list">
        <li>Plumbing</li><li>Hydro excavation</li><li>Hydro jetting</li><li>Well pumps</li>
        <li>Sewer pumps</li><li>Water mains</li><li>Sewer mains</li>
      </ul>
    </div>
  </section>

  <section class="card card-back">
    <div class="brand"><span class="brand-dot"></span>Kestrel Water &amp; Sewer</div>
    <div class="divider"></div>
    <div class="contact">
      <h1 class="person-name">Daniel Reyes</h1>
      <p class="person-role">CEO/Founder</p>
      <ul class="contact-list">
        <li><svg viewBox="0 0 24 24" aria-hidden="true"><path d="M6.6 10.8a15.1 15.1 0 0 0 6.6 6.6l2.2-2.2a1 1 0 0 1 1-.25 11.4 11.4 0 0 0 3.6.57 1 1 0 0 1 1 1V20a1 1 0 0 1-1 1A17 17 0 0 1 3 4a1 1 0 0 1 1-1h3.5a1 1 0 0 1 1 1c0 1.25.2 2.45.57 3.6a1 1 0 0 1-.25 1z"/></svg>845-555-0132</li>
        <li><svg viewBox="0 0 24 24" aria-hidden="true"><path d="M2 5h20v14H2zm2 2v.5l8 5 8-5V7l-8 5z"/></svg>info@kestrelws.com</li>
        <li><svg viewBox="0 0 24 24" aria-hidden="true"><path d="M12 2a10 10 0 1 0 0 20 10 10 0 0 0 0-20zm6.9 9h-3a15 15 0 0 0-1.3-5.6A8 8 0 0 1 18.9 11zM12 4.1c.9 1.3 1.7 3.8 1.9 6.9h-3.8c.2-3.1 1-5.6 1.9-6.9zM4.1 13h3a15 15 0 0 0 1.3 5.6A8 8 0 0 1 4.1 13zm3-2h-3a8 8 0 0 1 4.3-5.6A15 15 0 0 0 7.1 11zM12 19.9c-.9-1.3-1.7-3.8-1.9-6.9h3.8c-.2 3.1-1 5.6-1.9 6.9zm2.6-1.3a15 15 0 0 0 1.3-5.6h3a8 8 0 0 1-4.3 5.6z"/></svg>www.kestrelws.com</li>
      </ul>
    </div>
    <div class="offer">
      <p class="offer-line">We offer 24/7 emergency service</p>
      <ul class="bullet-list">
        <li>Residential</li><li>Commercial</li><li>Industrial</li><li>Municipal</li>
      </ul>
    </div>
  </section>
</body>
</html>
```